Modern Label Design needed for Virgin Coconut Oil bottle

Label for organic virgin coconut oil. Must be unique, creative, modern and give the impression of an expensive premium product.
Label is for round containers (bottles and jars) 250 ml, 500 ml and 750 ml.
The Brand name is "St. Orvane" and the product stated must include the words "organic" "cold-pressed" and "virgin coconut oil".
Label must include the following product description:
"St. Orvane virgin coconut oil is made from fresh mature coconuts harvested from organic farms across the Caribbean region. The oil is produced using the traditional natural fermentation method. Absolutely no heat is used in the process to allow for the maximum possible content of lauric acid."
Additional info: "Product of Tobago" "Manufactured and bottled by Marbeck Vale Ltd., Pelham Agro-Industrial Estate, Ferncliff Tobago".
Label must include room for Best Before date, Batch number, barcode and nutrition facts.
Colors can be at designer's discretion. However white, green and gold are preferred.

Target Market(s)

Women, Cosmetic Industry, (Food Industry to a lesser extent)

Industry/Entity Type

Product

Font styles to use
Script

Requirements
Must have
• An expensive look.
• The label is intended to have a transparent background
Nice to have
• The colors green and gold. However other color suggestions are welcome.
• Also, tasteful images that communicate an exotic tropical environment. (flowers, palms, coconuts

```html
<!DOCTYPE html>
<html lang="en">
<head>
<meta charset="utf-8">
<title>St. Orvane — Cold-Pressed Virgin Coconut Oil Label</title>
<link rel="stylesheet" href="https://fonts.googleapis.com/css2?family=Parisienne&family=Lora:ital@1&family=Alegreya:wght@400&family=Varela+Round&family=Arimo:wght@400&family=Tinos:wght@400&display=swap">
<style>
  :root {
    --cream: #f7f2d8;
    --cream-deep: #eee6c2;
    --cream-swirl: #faf7e6;
    --forest: #2f4c37;
    --forest-deep: #1f3627;
    --forest-light: #3b5c43;
    --wine: #7b1d1a;
    --wine-deep: #4a0d0b;
    --wine-light: #8e2a24;
    --ink: #1e1c17;
    --white: #ffffff;
  }
  html, body {
    margin: 0;
    padding: 0;
    width: 1200px;
    height: 600px;
    overflow: hidden;
    background: #ffffff;
  }
  .label {
    position: relative;
    width: 1200px;
    height: 600px;
    overflow: hidden;
  }
  .label__top {
    position: absolute;
    left: 0; top: 0;
    width: 1200px; height: 327px;
    background:
      radial-gradient(ellipse 420px 260px at 20% 30%, var(--cream-swirl), transparent 70%),
      radial-gradient(ellipse 380px 240px at 85% 60%, var(--cream-swirl), transparent 70%),
      linear-gradient(180deg, var(--cream) 0%, var(--cream-deep) 100%);
  }
  .label__bottom {
    position: absolute;
    left: 0; top: 327px;
    width: 1200px; height: 273px;
    background:
      radial-gradient(ellipse 500px 200px at 50% 40%, var(--forest-light), transparent 75%),
      linear-gradient(180deg, var(--forest-deep) 0%, var(--forest) 18%, var(--forest) 100%);
    box-shadow: inset 0 6px 10px rgba(0,0,0,0.45);
  }
  .brand-name {
    position: absolute;
    left: 0; width: 1176px;
    top: 88px;
    margin: 0;
    text-align: center;
    font-family: "Parisienne", cursive;
    font-weight: 400;
    font-size: 74px;
    line-height: 1;
    color: var(--wine);
  }
  .description {
    position: absolute;
    left: 843px;
    top: 139px;
    margin: 0;
    font-family: "Alegreya", serif;
    font-size: 16.8px;
    line-height: 25px;
    color: var(--ink);
  }
  .organic-badge {
    position: absolute;
    left: 472px;
    top: 271px;
    width: 226px;
    height: 106px;
  }
  .organic-badge__text {
    position: absolute;
    left: 0; top: 0;
    width: 226px; height: 106px;
    display: flex;
    align-items: center;
    justify-content: center;
    font-family: "Varela Round", sans-serif;
    font-size: 44px;
    color: var(--white);
    letter-spacing: 0.5px;
    padding-bottom: 6px;
    box-sizing: border-box;
  }
  .product-name {
    position: absolute;
    left: 0; width: 1176px;
    top: 401px;
    margin: 0;
    text-align: center;
    font-family: "Lora", serif;
    font-style: italic;
    font-weight: 400;
    font-size: 33px;
    line-height: 37px;
    color: var(--white);
  }
  .maker {
    position: absolute;
    left: 12px;
    top: 522px;
    margin: 0;
    font-family: "Tinos", serif;
    font-size: 16px;
    line-height: 21px;
    color: var(--white);
  }
  .volume {
    position: absolute;
    left: 727px;
    top: 559px;
    margin: 0;
    font-family: "Arimo", sans-serif;
    font-size: 26px;
    line-height: 30px;
    color: var(--white);
    letter-spacing: 0.5px;
  }
</style>
</head>
<body>
  <main class="label">
    <div class="label__top" role="img" aria-label="Cream background with a faint floral swirl damask pattern"></div>
    <div class="label__bottom" role="img" aria-label="Deep green band with a faint damask ornament pattern"></div>

    <h1 class="brand-name">St. Orvane</h1>

    <p class="description">
      St. Orvane virgin coconut oil is made from fresh<br>
      mature coconuts harvested from organic farms<br>
      across the Caribbean region.<br>
      The oil is produced using the traditional natural<br>
      fermentation method.<br>
      Absolutely no heat is used in the process to allow<br>
      for the maximum possible content of lauric acid.
    </p>

    <div class="organic-badge">
      <svg width="226" height="106" viewBox="0 0 226 106" aria-hidden="true">
        <defs>
          <radialGradient id="badgeFill" cx="50%" cy="35%" r="65%">
            <stop offset="0%" stop-color="#8e2a24"/>
            <stop offset="60%" stop-color="#6a1714"/>
            <stop offset="100%" stop-color="#4a0d0b"/>
          </radialGradient>
        </defs>
        <ellipse cx="113" cy="53" rx="110" ry="50" fill="#ffffff"/>
        <ellipse cx="113" cy="53" rx="105" ry="45" fill="url(#badgeFill)"/>
      </svg>
      <span class="organic-badge__text">organic</span>
    </div>

    <h2 class="product-name">Cold-Pressed<br>Virgin Coconut Oil</h2>

    <p class="maker">
      Product of Tobago<br>
      Manufactured and bottled by Marbeck Vale Ltd.,<br>
      Pelham Agro-Industrial Estate, Ferncliff Tobago
    </p>

    <p class="volume">250 ml</p>
  </main>
</body>
</html>
```